WP website design (Vorne)

We need a wordpress design for an established auction and real estate company based in Kentucky. The winning design will incorporate a professional color scheme with company logo in a clean layout with specified widgets. The design needs to consider that this will be developed on a responsive theme. Colors will complement the colors in the logo.

Industry/Entity Type

Real Estate

Font styles to use
Sans Serif

Requirements
Must have
• - Navigation:
1) Home 2) Auctions 3) Real Estate Listings 4) Our Services 5) Why Auctions 6) About Us 7) Past Auctions 8) Contact Us

Homeage will have slideshow, please use stock real estate image as the initial slide. Homepage will have this content: "Martin Vorne Auctioneer Real Estate Broker

Buying or selling you can count on Martin Vorne Auctioneer to deliver a quality auction experience. We handle all the details from initial handshake to final payment. We are with you every step of the way giving our sellers the service and results they deserve. You only have one chance for a successful auction. Contact us today to see how our experience and know-how can work for you. We are confident that you will appreciate our higher standard of service."

Footer will have smaller company logo, and attached association logos and this contact info:
Phone: (270) 555-0148
Contacts: Martin Vorne
Email: martinvorne@mailbrook.example
Address: 482 Pellworth Lane • Bowling Green, KY 42917

Widgets:
1) email sign up 2) Social media (twitter, video player - can also be in header 3) News & Events Blog widget 4) testimonials blog 5) Featured Video widget
Nice to have
• Nice to Have:
- demonstrate the drop-down menu styling, e.g. under Auctions
-Upcoming Auctions
-Online Auctions
-Past Auctions

```html
<!DOCTYPE html>
<html lang="en">
<head>
<meta charset="utf-8">
<title>Martin Vorne Auctioneer Real Estate Broker</title>
<link rel="stylesheet" href="https://fonts.googleapis.com/css2?family=Arimo:ital,wght@0,400;0,700;1,400&family=Source+Sans+3:wght@400;600;700&family=Raleway:wght@500&display=swap">
<style>
:root{
  --yellow:#f6c112;
  --blue:#2c5ea9;
  --blue-dark:#0f4f86;
  --text:#222;
  --panel:#f4f4f4;
  --line:#d9d9d9;
  --footer:#262626;
  --gold:#e4a90d;
}
*{box-sizing:border-box;margin:0;padding:0}
html,body{width:1107px;height:1200px;overflow:hidden;background:#fff}
body{position:relative;font-family:"Arimo",Arial,sans-serif;color:var(--text)}
.abs{position:absolute}

/* header */
.site-header{left:0;top:0;width:1107px;height:125px;background:var(--yellow)}
.brand{left:95px;top:36px;display:flex;align-items:center;gap:10px}
.brand-mark{width:26px;height:26px;background:var(--blue)}
.brand-name{font-family:"Source Sans 3",sans-serif;font-weight:700;font-size:30px;color:var(--blue);line-height:1}
.social{left:719px;top:17px;display:flex;align-items:center}
.social-label{font-family:"Source Sans 3",sans-serif;font-weight:700;font-size:14px;letter-spacing:.5px;margin-right:22px}
.social-dot{width:34px;height:34px;border-radius:50%;margin-right:8px}
.search{left:845px;top:78px;width:155px;height:24px;background:#fff;border:1px solid #ddd;font-size:12px;color:#888;padding:4px 6px}
.search-btn{position:absolute;right:1px;top:1px;width:22px;height:20px;background:var(--blue)}

/* nav */
.main-nav{left:0;top:125px;width:1107px;height:40px;background:var(--blue)}
.nav-item{position:absolute;top:12px;color:#fff;font-size:13px;white-space:nowrap}
.nav-sep{position:absolute;top:9px;width:1px;height:24px;background:#1a477f}

/* hero */
.hero{left:0;top:165px;width:1107px;height:435px;background:linear-gradient(180deg,#5d9bd6 0%,#a9cdea 35%,#d8c9b0 60%,#8a9d5a 85%,#5f9a2c 100%)}
.dropdown{left:151px;top:174px;width:129px;height:102px;background:rgba(95,108,130,.92);border-radius:4px;padding:9px 4px}
.dropdown::before{content:"";position:absolute;left:56px;top:-7px;border:7px solid transparent;border-top:0;border-bottom-color:rgba(95,108,130,.92)}
.drop-item{height:22px;color:#fff;font-size:11px;line-height:22px;padding:0 0 0 20px;position:relative;margin-bottom:9px;border-bottom:1px dotted #9aa4b5;white-space:nowrap}
.drop-item::before{content:"»";position:absolute;left:7px;top:0;font-weight:700}
.drop-item.active{background:var(--blue-dark);border-bottom:0}
.signup{left:744px;top:239px;width:262px;height:263px;background:rgba(240,242,245,.93);border-radius:6px;box-shadow:0 0 6px rgba(0,0,0,.25);padding:16px 16px}
.signup h2{font-family:"Raleway",sans-serif;font-weight:500;font-size:24px;color:var(--blue);margin:0 0 20px 2px;white-space:nowrap}
.field{height:36px;border:1px solid #ddd;border-radius:18px;background:#f7f7f7;font-size:13px;color:#333;padding:9px 15px;margin-bottom:14px;box-shadow:inset 0 1px 2px rgba(0,0,0,.08)}
.subscribe{position:absolute;right:20px;bottom:15px;width:105px;height:30px;border-radius:9px;background:linear-gradient(#f9cf2a,#e1a40a);font-family:"Source Sans 3",sans-serif;font-weight:700;font-size:15px;color:#222;text-align:center;line-height:30px}

/* tabs */
.tab{top:622px;height:38px;border-radius:5px 5px 0 0;font-family:"Source Sans 3",sans-serif;font-weight:600;font-size:19px;line-height:38px;padding:0 10px;white-space:nowrap;overflow:hidden;background:linear-gradient(#f3f3f3,#d6d6d6);color:#333;border:1px solid #ccc;border-bottom:0}
.tab.active{background:var(--blue);color:#fff;border-color:var(--blue)}
.blog{left:109px;top:660px;width:612px;height:278px;background:var(--panel);border:1px solid var(--line);border-radius:0 4px 4px 4px}
.blog-photo{left:12px;top:15px;width:181px;height:122px;background:linear-gradient(180deg,#9fc8e6,#3fa7bd 55%,#c6b8a0)}
.blog-title{left:208px;top:17px;font-family:"Source Sans 3",sans-serif;font-weight:400;font-size:15px;color:#222}
.blog-date{left:208px;top:38px;font-size:10.5px;color:var(--gold)}
.blog-lead{left:208px;top:56px;width:393px;font-size:11.3px;line-height:16.6px;text-align:justify}
.blog-body{left:12px;top:154px;width:589px;font-size:11.3px;line-height:16.6px;letter-spacing:.3px;text-align:justify}
.read-more{right:10px;bottom:8px;background:var(--blue-dark);color:#fff;font-size:11.5px;padding:2px 6px;border-radius:5px}

/* sidebar */
.video{left:744px;top:625px;width:253px;height:188px;background:linear-gradient(180deg,#1a1a1a 0,#1a1a1a 8%,#6d8a4c 10%,#88a06a 45%,#4c6b3c 70%,#1a1a1a 91%)}
.video-top{position:absolute;right:8px;top:4px;font-size:6px;color:#ddd}
.video-play{position:absolute;left:100px;top:71px;width:50px;height:34px;background:#1a1a1a;border-radius:4px}
.video-play svg{position:absolute;left:16px;top:8px}
.video-bar{position:absolute;left:0;top:170px;width:253px;height:3px;background:#c00}
.video-time{position:absolute;left:55px;top:177px;font-size:6px;color:#ccc}
.newsletter-box{left:739px;top:830px;width:264px;height:108px;background:var(--panel);border:1px solid var(--line);padding:8px 9px}
.newsletter-box h3{font-family:"Source Sans 3",sans-serif;font-weight:600;font-size:19px;color:#222}
.email-input{position:absolute;left:12px;top:40px;width:168px;height:31px;background:#fff;border:1px solid #ddd;font-style:italic;font-size:13px;color:#999;padding:8px 6px}
.sign-btn{position:absolute;left:180px;top:40px;width:67px;height:31px;background:var(--blue-dark);color:#fff;font-size:13px;text-align:center;line-height:31px}

/* testimonials */
.testi-heading{left:115px;top:960px;font-family:"Source Sans 3",sans-serif;font-weight:600;font-size:19px;color:var(--blue-dark)}
.avatar{left:115px;top:1003px;width:68px;height:68px;border-radius:50%;border:3px solid #ececec;box-shadow:0 0 2px #999;background:linear-gradient(180deg,#a9c9e0,#8b8577 60%,#5b89a3)}
.testi-name{left:116px;top:1075px;font-size:11.5px;font-style:italic;text-decoration:underline;white-space:nowrap}
.quote-mark{font-family:Georgia,serif;font-size:34px;color:var(--blue-dark);font-weight:700;line-height:1}
.testi-text{left:208px;top:992px;width:787px;font-size:11.3px;font-style:italic;line-height:16.6px;letter-spacing:.3px;text-align:justify;color:#222}

/* footer */
.site-footer{left:0;top:1122px;width:1107px;height:78px;background:var(--footer);color:#fff;font-size:11.5px;line-height:18.5px}
.footer-left{position:absolute;left:109px;top:17px}
.footer-right{position:absolute;right:96px;top:12px;text-align:right}
</style>
</head>
<body>

<header class="site-header abs">
  <div class="brand abs"><span class="brand-mark"></span><span class="brand-name">Martin Vorne</span></div>
  <div class="social abs">
    <span class="social-label">SOCIAL MEDIA:</span>
    <span class="social-dot" style="background:#184a7a"></span>
    <span class="social-dot" style="background:#1ba1e2"></span>
    <span class="social-dot" style="background:#ee7a12"></span>
    <span class="social-dot" style="background:#bcbcbc"></span>
  </div>
  <div class="search abs">search..
    <span class="search-btn"><svg width="22" height="20" viewBox="0 0 22 20"><circle cx="10" cy="9" r="4.5" fill="none" stroke="#fff" stroke-width="2"/><line x1="13" y1="12" x2="16.5" y2="15.5" stroke="#fff" stroke-width="2"/></svg></span>
  </div>
</header>

<nav class="main-nav abs">
  <span class="nav-item" style="left:115px">Home</span><span class="nav-sep" style="left:167px"></span>
  <span class="nav-item" style="left:187px">Auctions</span><span class="nav-sep" style="left:255px"></span>
  <span class="nav-item" style="left:276px">Real Estate Listings</span><span class="nav-sep" style="left:410px"></span>
  <span class="nav-item" style="left:428px">Our Services</span><span class="nav-sep" style="left:522px"></span>
  <span class="nav-item" style="left:541px">Why Auctions</span><span class="nav-sep" style="left:638px"></span>
  <span class="nav-item" style="left:656px">About Us</span><span class="nav-sep" style="left:729px"></span>
  <span class="nav-item" style="left:748px">Past Auctions</span><span class="nav-sep" style="left:847px"></span>
  <span class="nav-item" style="left:868px">Contact Us</span>
</nav>

<section class="hero abs" role="img" aria-label="Stock photo of a two-storey brick and stucco family home with a green lawn under a blue sky"></section>

<div class="dropdown abs">
  <div class="drop-item active">Online Auctions</div>
  <div class="drop-item">Upcoming Auctions</div>
  <div class="drop-item" style="border-bottom:0">Past Auctions</div>
</div>

<form class="signup abs">
  <h2>Newsletter Sign Up</h2>
  <div class="field">First Name</div>
  <div class="field">Last Name</div>
  <div class="field">Email Address</div>
  <div class="subscribe">SUBSCRIBE</div>
</form>

<div class="tab active abs" style="left:109px;width:183px">News &amp; Events Blog</div>
<div class="tab abs" style="left:300px;width:148px">Auction Results</div>
<div class="tab abs" style="left:457px;width:162px">Alliance Auctions</div>

<article class="blog abs">
  <div class="blog-photo abs" role="img" aria-label="Photo of a turquoise single-storey house with a covered porch"></div>
  <h4 class="blog-title abs">Upcoming Auctions</h4>
  <div class="blog-date abs">May 15, 2012</div>
  <p class="blog-lead abs"><b>Lorem Ipsum is simply dummy text</b> of the printing and typesetting industry. Lorem Ipsum has been the industry's standard dummy text ever since the 1500s, when an unknown printer took a galley of type and scrambled it to make a type specimen book. It has survived not only five centuries, but also the leap into electronic typesetting.</p>
  <p class="blog-body abs">Lorem Ipsum is simply dummy text of the printing and typesetting industry. Lorem Ipsum has been the industry's standard dummy text ever since the 1500s, when an unknown printer took a galley of type and scrambled it to make a type specimen book. It has survived not only five centuries, but also the leap into electronic typesetting Lorem Ipsum is simply dummy text of the printing and typesetting industry. Lorem Ipsum has been the industry's standard dummy text ever since the 1500s, when an unknown printer took a galley of type and scrambled it to make a type specimen book.</p>
  <span class="read-more abs">read more</span>
</article>

<aside class="video abs" role="img" aria-label="Featured video of trees reflected in a calm lake">
  <span class="video-top">Share &nbsp; More info</span>
  <span class="video-play"><svg width="18" height="18" viewBox="0 0 18 18"><path d="M2 1 L17 9 L2 17 Z" fill="#fff"/></svg></span>
  <span class="video-bar"></span>
  <span class="video-time">0:00</span>
</aside>

<aside class="newsletter-box abs">
  <h3>Contact Circle</h3>
  <div class="email-input">Email</div>
  <div class="sign-btn">Sign Up</div>
</aside>

<h3 class="testi-heading abs">Testimonials</h3>
<div class="avatar abs" role="img" aria-label="Round portrait thumbnail of the reviewer"></div>
<div class="testi-name abs">Corla Benning</div>
<span class="quote-mark abs" style="left:184px;top:990px">&ldquo;</span>
<p class="testi-text abs">Lorem Ipsum is simply dummy text of the printing and typesetting industry. Lorem Ipsum has been the industry's standard dummy text ever since the 1500s, when an unknown printer took a galley of type and scrambled it to make a type specimen book. It has survived not only five centuries, but also the leap into electronic typesetting Lorem Ipsum is simply dummy text of the printing and typesetting industry. Lorem Ipsum has been the industry's standard dummy text ever but also the leap into electronic typesetting Lorem Ipsum is simply dummy text of the printing and typesetting industry. Lorem Ipsum has been the industry's standard since the 1500s, when an unknown printer took a galley....</p>
<span class="quote-mark abs" style="left:837px;top:1066px">&rdquo;</span>

<footer class="site-footer abs">
  <div class="footer-left">Copyright © 2007 - 2014 - Martin Vorne Auctioneer Real Estate Broker. - All Rights Reserved<br>Powered by: BidHallway.example and GavelRegistry.example</div>
  <div class="footer-right">Phone: (270) 555-0148<br>Email: martinvorne@mailbrook.example<br>482 Pellworth Lane • Bowling Green, KY 42917</div>
</footer>

</body>
</html>
```